Stationary design for real estate company in Trinidad and Tobago

Kestra Realty Ltd. , real estate company operating in Trinidad and Tobago, requires a sleek, modern and professional stationary package to wow our customers and potential new clients. we want to look sleek and professional; first impressions count in this business!
Business Address:
Level 1, Marlowe Point Tower
4C Seldon Grove Boulevard
Marlowe Point
Colwyn Pereira Highway
Port of Spain
Trinidad
Tel: + 1 868 555 0147
www.kestra-tt.com
info@kestra-tt.com

```html
<!DOCTYPE html>
<html lang="en">
<head>
<meta charset="utf-8">
<title>Kestra Realty – Business Card</title>
<link href="https://fonts.googleapis.com/css2?family=Roboto:wght@300;400;500;700&display=swap" rel="stylesheet">
<style>
  :root {
    --navy: #1b3058;
    --navy-deep: #172a4e;
    --gold: #c9a35a;
    --cream: #f3efe3;
    --ink-grey: #5a5a5a;
    --silver: #c7c9d3;
    --backdrop: #1a1a1c;
  }
  * { margin: 0; padding: 0; box-sizing: border-box; }
  html, body {
    width: 1200px; height: 988px; overflow: hidden;
    background: var(--backdrop);
    font-family: "Roboto", sans-serif;
  }
  .sheet {
    width: 1200px; height: 988px;
    display: flex; flex-direction: column;
    align-items: center; justify-content: center; gap: 40px;
  }
  .card {
    width: 760px; height: 434px;
    position: relative;
    box-shadow: 0 10px 30px rgba(0,0,0,.5);
  }
  /* Front */
  .card--front { background: var(--cream); }
  .wordmark {
    position: absolute;
    display: flex; align-items: center; gap: 14px;
  }
  .wordmark__dot {
    width: 34px; height: 34px; border-radius: 50%;
    background: var(--gold);
  }
  .wordmark__name {
    font-weight: 400; letter-spacing: .16em; text-transform: uppercase;
    white-space: nowrap;
  }
  .card--front .wordmark { top: 78px; left: 322px; }
  .card--front .wordmark__name { font-size: 38px; color: var(--navy); }

  .person {
    position: absolute; top: 210px; right: 430px;
    text-align: right;
  }
  .person__name {
    font-weight: 700; font-size: 22px; color: var(--navy);
    text-transform: uppercase; letter-spacing: .01em;
  }
  .person__role {
    font-weight: 400; font-size: 20px; color: var(--gold);
    margin-top: 4px;
  }
  .divider {
    position: absolute; top: 200px; left: 348px;
    width: 1px; height: 108px; background: #9a9a9a;
  }
  .contacts {
    position: absolute; top: 204px; left: 368px;
    list-style: none;
  }
  .contacts li {
    display: flex; align-items: center; gap: 10px;
    font-size: 20px; color: var(--ink-grey);
    line-height: 33px;
  }
  .contacts svg { width: 18px; height: 18px; flex: none; }
  .address {
    position: absolute; left: 60px; right: 40px; top: 336px;
    font-size: 19px; font-weight: 400; color: var(--ink-grey);
    line-height: 28px;
  }
  /* Back */
  .card--back {
    background: var(--navy-deep);
    display: flex; align-items: center; justify-content: center;
  }
  .card--back .wordmark { position: static; }
  .card--back .wordmark__name { font-size: 48px; color: var(--silver); }
</style>
</head>
<body>
<main class="sheet">
  <section class="card card--front" aria-label="Business card front">
    <div class="wordmark">
      <span class="wordmark__dot"></span>
      <span class="wordmark__name">Kestra Realty</span>
    </div>

    <div class="person">
      <p class="person__name">Anders Lindqvist</p>
      <p class="person__role">Founder &amp; CEO</p>
    </div>

    <div class="divider"></div>

    <ul class="contacts">
      <li>
        <svg viewBox="0 0 24 24" aria-hidden="true"><path fill="var(--gold)" d="M6.6 10.8a15.1 15.1 0 0 0 6.6 6.6l2.2-2.2a1 1 0 0 1 1-.25 11.4 11.4 0 0 0 3.6.57 1 1 0 0 1 1 1V20a1 1 0 0 1-1 1A17 17 0 0 1 3 4a1 1 0 0 1 1-1h3.5a1 1 0 0 1 1 1c0 1.25.2 2.45.57 3.57a1 1 0 0 1-.25 1z"/></svg>
        + 1 868 555 0147
      </li>
      <li>
        <svg viewBox="0 0 24 24" aria-hidden="true"><rect x="2" y="5" width="20" height="14" fill="none" stroke="var(--gold)" stroke-width="2"/><path d="M2 5l10 8 10-8" fill="none" stroke="var(--gold)" stroke-width="2"/></svg>
        info@kestra-tt.com
      </li>
      <li>
        <svg viewBox="0 0 24 24" aria-hidden="true"><g fill="none" stroke="var(--gold)" stroke-width="1.8"><circle cx="12" cy="12" r="9.5"/><ellipse cx="12" cy="12" rx="4" ry="9.5"/><path d="M2.5 12h19M4 7h16M4 17h16"/></g></svg>
        www.kestra-tt.com
      </li>
    </ul>

    <p class="address">
      Level 1, Marlowe Point Tower 4C Seldon Grove Boulevard<br>
      Marlowe Point Colwyn Pereira Highway Port of Spain Trinidad
    </p>
  </section>

  <section class="card card--back" aria-label="Business card back">
    <div class="wordmark">
      <span class="wordmark__dot"></span>
      <span class="wordmark__name">Kestra Realty</span>
    </div>
  </section>
</main>
</body>
</html>
```